Redesign Two Website Pages (Homepage & Features) — Modern, Responsive, and Visually Engaging

We’re looking to redesign two pages of our website:

Homepage: https://velmorak.com
Features Page: https://velmorak.com/features

We already have a preliminary design in Figma for the homepage, but it currently feels too plain. Please don’t use this Figma file provided. It was only shared for facilitate using the current website content and not as a source for inspiration. Use your creativity to bring something fresh and less dull as the current design.

We want to enhance it with visually engaging elements, such as illustrations, graphics, or images that align with the content and the application’s purpose, making the design more dynamic and marketing-oriented.

Requirements:
- Create modern, visually appealing designs for both pages.
- Include relevant visuals (images or vector graphics) that complement the content and improve user engagement.
- Ensure full responsiveness across all major viewports: desktop, tablet, and mobile.
- Deliver the final design in Figma format.
- You can choose any colour palette that best fits the concept, but please retain the existing content from the live website.
- We’re looking for a clean, modern, and commercially appealing design that effectively communicates the value of our product.

Target Market(s)

B2B

Number of Pages Required

2 page

Font styles to use
Sans Serif

Requirements
Must have
• Images and graphics to make the design and product more attractive.

```html
<!DOCTYPE html>
<html lang="en">
<head>
<meta charset="utf-8">
<title>Velmorak — Features</title>
<link href="https://fonts.googleapis.com/css2?family=Inter:wght@400;500;600;700&display=swap" rel="stylesheet">
<style>
:root{
  --navy:#061a38;
  --navy-2:#0b2f5e;
  --blue:#1565c0;
  --bright:#1e88e5;
  --sky:#dceefc;
  --sky-2:#a9d2f3;
  --ink:#0b1b30;
  --white:#ffffff;
  --muted:#b8c8de;
  --line:#7fb3e6;
}
*{box-sizing:border-box;margin:0;padding:0}
html,body{width:1200px;height:2904px;overflow:hidden}
body{font-family:"Inter",sans-serif;color:var(--ink);background:var(--navy);position:relative}
.abs{position:absolute}

/* hero */
.hero{position:absolute;left:0;top:0;width:1200px;height:481px;background:linear-gradient(115deg,#0c3a75 0%,#0a2d5c 40%,#061d40 75%,#061631 100%);overflow:hidden;color:var(--white)}
.hero-shade{position:absolute;left:150px;top:-40px;width:260px;height:600px;background:rgba(255,255,255,.04);transform:skewX(-18deg)}
.nav{position:absolute;left:113px;top:38px;width:974px;height:54px;border-bottom:1px solid rgba(255,255,255,.35)}
.brand{position:absolute;left:0;top:4px;display:flex;align-items:center;gap:10px}
.brand-dot{width:22px;height:22px;border-radius:50%;background:var(--white)}
.brand-name{font-size:14px;font-weight:500;letter-spacing:.4px;line-height:16px}
.brand-tag{font-size:10.5px;opacity:.85;line-height:13px}
.nav-links{position:absolute;left:400px;top:13px;display:flex;gap:28px;font-size:12px;font-weight:500}
.nav-links .active{text-decoration:underline;text-underline-offset:4px}
.nav-auth{position:absolute;right:0;top:4px;display:flex;align-items:center;gap:13px;font-size:11px;font-weight:500}
.pill{display:inline-flex;align-items:center;gap:14px;border-radius:20px;padding:0 5px 0 20px;height:34px}
.pill .arr{width:22px;height:22px;border-radius:50%;display:flex;align-items:center;justify-content:center}
.pill-blue{background:var(--bright);color:var(--white)}
.pill-blue .arr{background:var(--white);color:var(--bright)}
.hero-eyebrow{position:absolute;left:112px;top:178px;font-size:15.5px;font-weight:500}
.hero-title{position:absolute;left:111px;top:216px;font-size:45px;line-height:50px;font-weight:700;letter-spacing:-.5px}
.hero-copy{position:absolute;left:112px;top:326px;width:420px;font-size:15.5px;line-height:24.5px;color:#e6eef8}
.tile{position:absolute;border-radius:16px;background:linear-gradient(160deg,#143e70,#0d2a52);box-shadow:0 6px 20px rgba(0,0,0,.3);font-size:7px;color:#cfe0f5}

/* features */
.features{position:absolute;left:0;top:481px;width:1200px;height:699px;background:var(--white)}
.features::after{content:"";position:absolute;left:0;bottom:0;width:1200px;height:40px;background:linear-gradient(#fff,#e3f1fd)}
.feat-title{position:absolute;left:111px;top:232px;font-size:37px;line-height:42px;font-weight:600}
.feat-title span{color:var(--blue)}
.feat-copy{position:absolute;left:111px;top:326px;width:390px;font-size:15px;line-height:23px;color:#2a3a4f}
.btn-row{position:absolute;left:112px;top:426px;display:flex;gap:8px}
.btn{display:inline-flex;align-items:center;gap:26px;height:41px;border-radius:22px;padding:0 6px 0 19px;font-size:12px;font-weight:500;letter-spacing:.2px}
.btn .arr{width:26px;height:26px;border-radius:50%;display:flex;align-items:center;justify-content:center}
.btn-solid{background:var(--blue);color:#fff}
.btn-solid .arr{background:#fff;color:var(--blue)}
.btn-outline{border:1.5px solid var(--blue);color:var(--blue);background:#fff}
.btn-outline .arr{background:var(--blue);color:#fff}
.sketch{position:absolute;left:25px;top:504px;width:300px;height:195px;background:linear-gradient(180deg,#f4f8fc,#e3eef9);border-radius:8px}
.feature-card{position:absolute;left:585px;top:65px;width:501px;height:572px;border-radius:18px;background:linear-gradient(180deg,#e6f3fd,#bfe0f9)}
.photo{position:absolute;left:32px;top:49px;width:253px;height:271px;border-radius:10px;background:linear-gradient(140deg,#2d3f55,#0d1a2b 60%,#1e2e45)}
.chart-pop{position:absolute;left:240px;top:128px;width:226px;height:167px;border-radius:8px;background:#0a1c48;border:3px solid #fff}
.card-icon{position:absolute;left:28px;top:356px;width:40px;height:40px;border-radius:50%;background:#0f2f57;display:flex;align-items:center;justify-content:center}
.card-head{position:absolute;left:82px;top:363px;font-size:21px;font-weight:500}
.card-copy{position:absolute;left:28px;top:413px;width:450px;font-size:12.5px;line-height:19px;color:#2a3a4f}
.tags{position:absolute;left:28px;top:461px;width:450px;display:flex;flex-wrap:wrap;gap:13px 12px}
.tag{height:31px;border-radius:16px;background:#071a33;color:#fff;font-size:11.5px;display:flex;align-items:center;padding:0 24px}

/* enterprise */
.enterprise{position:absolute;left:0;top:1180px;width:1200px;height:523px;background:linear-gradient(100deg,#0b2c5a,#061a3a 50%,#041330);color:#fff}
.sec-title{position:absolute;left:0;width:1200px;text-align:center;font-size:38px;font-weight:600}
.sec-title .hl{color:#2f95f1}
.sec-sub{position:absolute;left:0;width:1200px;text-align:center;font-size:15px}
.cap-card{position:absolute;top:153px;width:430px;height:288px;border-radius:8px;background:linear-gradient(180deg,#eef7ff,#dcedfc);border:2px solid #4fa4ee;color:var(--ink)}
.cap-icon{position:absolute;left:24px;top:20px;width:48px;height:48px;border-radius:50%;background:linear-gradient(160deg,#2e86de,#0b3b7a);display:flex;align-items:center;justify-content:center}
.cap-card h3{position:absolute;left:24px;top:91px;font-size:26px;font-weight:500}
.cap-card ul{position:absolute;left:24px;top:136px;list-style:none;font-size:16.5px;line-height:35px}
.cap-card li::before{content:"";display:inline-block;width:7px;height:7px;border-radius:50%;background:var(--bright);box-shadow:0 0 0 2px #cfe5fb;margin-right:9px;vertical-align:middle}
.hub{position:absolute;left:510px;top:214px;width:166px;height:166px;border-radius:50%;background:linear-gradient(150deg,#3b8fdc,#0d3f86);border:5px solid #fff}

/* why */
.why{position:absolute;left:0;top:1703px;width:1200px;height:642px;background:linear-gradient(160deg,#1c73cf,#0e57b3 60%,#0b4aa0);overflow:hidden;color:#fff}
.why-base{position:absolute;left:0;top:330px;width:1200px;height:320px;background:var(--navy)}
.why-wave{position:absolute;left:0;top:240px}
.table{position:absolute;left:112px;top:152px;width:974px;border-collapse:collapse;background:#fff;color:var(--ink);border-radius:8px;overflow:hidden;box-shadow:0 0 0 2px #8ec6f3}
.table th{height:57px;background:#a9d1f1;font-size:23px;font-weight:500}
.table td{height:53px;text-align:center;font-size:15px;border-top:1px solid var(--line)}
.table td:first-child{background:#eaf4fd}
.table td+td,.table th+th{border-left:1px solid var(--line)}

/* cta */
.cta{position:absolute;left:114px;top:2345px;width:975px;height:311px;border-radius:10px;background:linear-gradient(110deg,#0d6bd1,#3f98e4 60%,#63aeea);color:#fff;overflow:hidden}
.cta h2{position:absolute;left:71px;top:54px;font-size:37px;line-height:43px;font-weight:600}
.cta p{position:absolute;left:68px;top:154px;width:280px;font-size:15.5px;line-height:23px}
.cta .btn-row{left:69px;top:213px}
.btn-white{background:#fff;color:var(--ink)}
.btn-white .arr{background:var(--blue);color:#fff}
.btn-ghost{border:1.5px solid #fff;color:#fff}
.btn-ghost .arr{border:1.5px solid #fff;color:#fff}

/* footer */
.footer{position:absolute;left:0;top:2656px;width:1200px;height:248px;background:var(--navy);color:#fff}
.foot-about{position:absolute;left:195px;top:42px;width:240px}
.foot-about p{margin-top:20px;font-size:10px;line-height:15px;color:var(--muted)}
.foot-col{position:absolute;top:46px}
.foot-col h4{font-size:16px;font-weight:500;margin-bottom:14px}
.foot-col a{display:block;font-size:10px;color:var(--muted);text-decoration:none;line-height:23.5px}
.foot-rule{position:absolute;left:114px;top:207px;width:975px;border-top:1px solid rgba(255,255,255,.4)}
.copyright{position:absolute;left:0;top:222px;width:1200px;text-align:center;font-size:11px}
</style>
</head>
<body>

<section class="hero">
  <div class="hero-shade"></div>
  <nav class="nav">
    <div class="brand"><span class="brand-dot"></span><div><div class="brand-name">VELMORAK</div><div class="brand-tag">Guiding every audit with clarity</div></div></div>
    <div class="nav-links"><span class="active">Features</span><span>Pricing</span><span>Demo</span></div>
    <div class="nav-auth"><span>SIGN UP</span><span class="pill pill-blue">SIGN IN <span class="arr">→</span></span></div>
  </nav>
  <p class="hero-eyebrow">Everything you need for modern auditing</p>
  <h1 class="hero-title">Your Fleet Smarter.<br>Safer. Stronger.</h1>
  <p class="hero-copy">Discover the features that transform how you manage vehicles—from tracking performance and optimising efficiency to reducing disruptions and boosting uptime.</p>

  <div class="tile" style="left:582px;top:175px;width:178px;height:105px;overflow:hidden">
    <div style="padding:8px 14px">12:30</div>
    <div style="text-align:center;font-size:14px;color:#fff;font-weight:500">Welcome</div>
    <div style="position:absolute;left:0;bottom:0;width:178px;height:38px;background:#2a8ae8;border-radius:0 0 16px 16px;display:flex;justify-content:space-around;align-items:center"><i style="width:10px;height:10px;background:#fff;border-radius:2px"></i><i style="width:10px;height:10px;background:#fff;border-radius:50%"></i><i style="width:10px;height:10px;background:#fff;border-radius:50%"></i><i style="width:12px;height:3px;background:#fff"></i></div>
  </div>
  <div class="tile" style="left:582px;top:298px;width:178px;height:200px">
    <div style="padding:18px 16px 8px;color:#fff">Transaction history</div>
    <div style="margin:0 12px;height:40px;border-radius:8px;background:#2a8ae8;color:#fff;font-size:14px;padding:10px 14px">$130</div>
    <div style="margin:12px 28px;font-size:14px;color:#6f8fb5">$240</div>
    <div style="margin:14px 28px;font-size:14px;color:#6f8fb5">$169</div>
  </div>
  <div class="tile" style="left:787px;top:175px;width:178px;height:188px">
    <div style="padding:14px 14px;color:#fff">Statistics</div>
    <svg class="abs" style="left:12px;top:30px" width="154" height="140" viewBox="0 0 154 140">
      <g stroke-width="5" stroke-linecap="round">
        <line x1="4" y1="130" x2="4" y2="50" stroke="#2f8ae6"/><line x1="4" y1="45" x2="4" y2="30" stroke="#e02b2b"/>
        <line x1="24" y1="130" x2="24" y2="70" stroke="#2f8ae6"/><line x1="24" y1="62" x2="24" y2="40" stroke="#e02b2b"/>
        <line x1="44" y1="130" x2="44" y2="80" stroke="#2f8ae6"/><line x1="44" y1="72" x2="44" y2="30" stroke="#e02b2b"/>
        <line x1="64" y1="130" x2="64" y2="60" stroke="#2f8ae6"/><line x1="64" y1="52" x2="64" y2="8" stroke="#e02b2b"/>
        <line x1="84" y1="130" x2="84" y2="70" stroke="#2f8ae6"/><line x1="84" y1="62" x2="84" y2="50" stroke="#e02b2b"/>
        <line x1="104" y1="130" x2="104" y2="55" stroke="#2f8ae6"/><line x1="104" y1="47" x2="104" y2="38" stroke="#e02b2b"/>
        <line x1="124" y1="130" x2="124" y2="60" stroke="#2f8ae6"/><line x1="124" y1="52" x2="124" y2="38" stroke="#e02b2b"/>
        <line x1="144" y1="130" x2="144" y2="50" stroke="#2f8ae6"/><line x1="144" y1="42" x2="144" y2="18" stroke="#e02b2b"/>
      </g>
    </svg>
  </div>
  <div class="tile" style="left:787px;top:390px;width:178px;height:110px">
    <div style="padding:12px 14px;color:#fff">Monthly Transaction</div>
    <div style="margin:2px 0 0 36px;width:120px;height:4px;background:#2f8ae6;border-radius:2px"></div>
    <div style="margin:5px 0 0 36px;width:52px;height:4px;background:#e02b2b;border-radius:2px"></div>
    <div style="margin:18px 0 0 36px;width:120px;height:4px;background:#2f8ae6;border-radius:2px"></div>
    <div style="margin:5px 0 0 36px;width:52px;height:4px;background:#e02b2b;border-radius:2px"></div>
  </div>
  <div class="tile" style="left:986px;top:175px;width:178px;height:58px">
    <div style="position:absolute;left:14px;top:20px;width:18px;height:18px;border-radius:5px;background:#6f8fb5"></div>
    <div style="position:absolute;left:44px;top:20px;font-size:11px;color:#fff">3</div>
    <div style="position:absolute;left:60px;top:20px;width:18px;height:18px;border-radius:5px;background:#6f8fb5"></div>
    <div style="position:absolute;left:100px;top:19px;width:64px;height:20px;border-radius:5px;background:#2f8ae6;color:#fff;font-size:6px;text-align:center;line-height:20px">Add to cart</div>
  </div>
  <div class="tile" style="left:986px;top:248px;width:178px;height:100px">
    <div style="padding:12px 14px;color:#fff">Market comparison</div>
    <svg class="abs" style="left:16px;top:32px" width="56" height="56" viewBox="0 0 56 56"><circle cx="28" cy="28" r="22" fill="none" stroke="#2f8ae6" stroke-width="5"/><path d="M28 6a22 22 0 0 1 20 30" fill="none" stroke="#e02b2b" stroke-width="5"/><circle cx="28" cy="28" r="12" fill="none" stroke="#1b4f8a" stroke-width="3"/></svg>
    <div style="position:absolute;left:90px;top:60px;font-size:18px;color:#fff;font-weight:500">$35,903</div>
  </div>
  <div class="tile" style="left:986px;top:360px;width:178px;height:62px">
    <div style="position:absolute;left:16px;top:12px;color:#fff">Set credit limit</div>
    <div style="position:absolute;right:16px;top:9px;font-size:12px;color:#5fb0ff">$1670</div>
    <div style="position:absolute;left:16px;top:34px;width:146px;height:3px;background:#3c5f88;border-radius:2px"><div style="width:96px;height:3px;background:#5fb0ff"></div></div>
    <div style="position:absolute;left:16px;top:44px">$0</div><div style="position:absolute;right:16px;top:44px">$2000</div>
  </div>
  <div class="tile" style="left:986px;top:434px;width:178px;height:70px;overflow:hidden">
    <div style="padding:10px 16px;color:#fff">Market popularity</div>
    <svg class="abs" style="left:0;top:10px" width="178" height="60" viewBox="0 0 178 60"><path d="M10 50C30 40 40 50 60 40S90 50 110 35 140 10 160 20" fill="none" stroke="#2f8ae6" stroke-width="3"/><circle cx="160" cy="20" r="4" fill="#fff"/></svg>
  </div>
</section>

<section class="features">
  <h2 class="feat-title">Powerful Features for<br><span>Effortless Auditing</span></h2>
  <p class="feat-copy">From AI-powered templates to real-time collaboration, Velmorak provides all the tools you need to conduct thorough, efficient audits.</p>
  <div class="btn-row">
    <span class="btn btn-solid">START FREE TRIAL <span class="arr">→</span></span>
    <span class="btn btn-outline">SCHEDULE DEMO <span class="arr">→</span></span>
  </div>
  <div class="sketch" role="img" aria-label="Line drawing of an auditor working on a laptop"></div>

  <div class="feature-card">
    <div class="photo" role="img" aria-label="Photo of an analyst wearing headphones working at a desk under a lamp at night"></div>
    <div class="chart-pop">
      <div style="display:flex;justify-content:space-around;color:#c7d6ef;font-size:8px;padding:6px 8px 0"><span>Day</span><span style="color:#4aa8ff">Week</span><span>Month</span><span>Year</span></div>
      <div style="display:flex;justify-content:space-around;color:#8aa3c8;font-size:6px;padding:6px 4px 0"><span>January</span><span>February</span><span>March</span><span style="border:1px solid #fff;color:#fff;padding:0 4px;border-radius:3px">April</span><span>May</span></div>
      <svg class="abs" style="left:10px;top:50px" width="200" height="95" viewBox="0 0 200 95"><defs><linearGradient id="fillArea" x1="0" y1="0" x2="0" y2="1"><stop offset="0" stop-color="#2f8ae6" stop-opacity=".45"/><stop offset="1" stop-color="#2f8ae6" stop-opacity="0"/></linearGradient></defs><path d="M5 75C20 60 30 72 45 64S65 48 75 60 90 80 100 70 110 20 118 18 128 60 140 48 152 40 165 45 180 28 195 30V95H5Z" fill="url(#fillArea)"/><path d="M5 75C20 60 30 72 45 64S65 48 75 60 90 80 100 70 110 20 118 18 128 60 140 48 152 40 165 45 180 28 195 30" fill="none" stroke="#4aa8ff" stroke-width="2"/></svg>
      <div style="position:absolute;left:12px;bottom:4px;width:196px;display:flex;justify-content:space-between;font-size:5px;color:#8aa3c8"><span>1</span><span>2</span><span>3</span><span>4</span><span>5</span><span>6</span><span>7</span><span>8</span><span>9</span></div>
    </div>
    <div class="card-icon"><svg width="18" height="18" viewBox="0 0 18 18" fill="none" stroke="#fff" stroke-width="1.5"><rect x="4" y="4" width="10" height="10" rx="2"/><path d="M7 1v3M11 1v3M7 14v3M11 14v3M1 7h3M1 11h3M14 7h3M14 11h3"/></svg></div>
    <h3 class="card-head">AI-Powered Template Builder</h3>
    <p class="card-copy">Generate comprehensive audit templates in seconds with our intelligent AI assistant. Customize every aspect to match your specific requirements.</p>
    <div class="tags"><span class="tag">50+ pre-built templates</span><span class="tag">AI customization</span><span class="tag">Industry-specific frameworks</span><span class="tag">Version control</span></div>
  </div>
</section>

<section class="enterprise">
  <h2 class="sec-title" style="top:52px"><span class="hl">Enterprise</span>-Grade Capabilities</h2>
  <p class="sec-sub" style="top:111px">Built to handle the most demanding audit requirements</p>
  <div class="cap-card" style="left:113px">
    <div class="cap-icon"><svg width="26" height="26" viewBox="0 0 26 26" fill="none" stroke="#fff" stroke-width="1.6"><circle cx="13" cy="13" r="10"/><ellipse cx="13" cy="13" rx="4.5" ry="10"/><path d="M3 13h20M5 7.5h16M5 18.5h16"/></svg></div>
    <h3>Global Scale</h3>
    <ul><li>Multi-language support for global teams</li><li>Regional compliance frameworks</li><li>24/7 global support coverage</li><li>Data residency options</li></ul>
  </div>
  <div class="cap-card" style="left:656px">
    <div class="cap-icon"><svg width="24" height="24" viewBox="0 0 24 24" fill="none" stroke="#fff" stroke-width="1.6"><path d="M12 2l8 3v6c0 5-3.5 9-8 11-4.5-2-8-6-8-11V5z"/><rect x="9" y="11" width="6" height="5" rx="1"/><path d="M10 11V9a2 2 0 0 1 4 0v2"/></svg></div>
    <h3>Advanced Security</h3>
    <ul><li>Role-based access control (RBAC)</li><li>Single Sign-On (SSO) integration</li><li>IP whitelisting and MFA</li><li>Penetration tested quarterly</li></ul>
  </div>
  <div class="hub"></div>
</section>

<section class="why">
  <div class="why-base"></div>
  <svg class="why-wave" width="1200" height="130" viewBox="0 0 1200 130"><path d="M0 90C300 40 700 60 1200 0V130H0Z" fill="#061a38"/></svg>
  <h2 class="sec-title" style="top:52px">Why Choose Velmorak?</h2>
  <p class="sec-sub" style="top:105px">See how we compare to traditional audit methods</p>
  <table class="table">
    <thead><tr><th style="width:369px">Feature</th><th style="width:311px">Traditional Methods</th><th>VELMORAK</th></tr></thead>
    <tbody>
      <tr><td>Template Creation</td><td>Hours/Days</td><td>30 Seconds</td></tr>
      <tr><td>Team Collaboration</td><td>Email &amp; Spreadsheets</td><td>Real-time</td></tr>
      <tr><td>Evidence Management</td><td>Scattered Files</td><td>Centralized</td></tr>
      <tr><td>Compliance Tracking</td><td>Manual</td><td>Automated</td></tr>
      <tr><td>Report Generation</td><td>Manual Compilation</td><td>One-Click</td></tr>
      <tr><td>PII Detection</td><td>Manual Review</td><td>Automated AI</td></tr>
      <tr><td>Weight Calculation &amp; Scoring</td><td>Basic Formulas</td><td>Complex Scenarios</td></tr>
    </tbody>
  </table>
</section>

<section class="cta">
  <h2>Experience the<br>Power of Velmorak</h2>
  <p>See how these features can transform your audit process</p>
  <div class="btn-row">
    <span class="btn btn-white">START FREE TRIAL <span class="arr">→</span></span>
    <span class="btn btn-ghost">WATCH DEMO <span class="arr">→</span></span>
  </div>
</section>

<footer class="footer">
  <div class="foot-about">
    <div class="brand" style="position:static"><span class="brand-dot"></span><div><div class="brand-name">VELMORAK</div><div class="brand-tag">Guiding every audit with clarity</div></div></div>
    <p>The only audit platform that combines AI-powered template generation, real-time collaboration, and intelligent compliance tracking. Join leading firms completing audits 3x faster with 99.9% accuracy.</p>
  </div>
  <div class="foot-col" style="left:508px"><h4>Product</h4><a href="#">Features</a><a href="#">Pricing</a><a href="#">Demo</a><a href="#">Sign In</a></div>
  <div class="foot-col" style="left:700px"><h4>Company</h4><a href="#">About</a><a href="#">Contact</a><a href="#">System Status</a></div>
  <div class="foot-col" style="left:902px"><h4>Legal</h4><a href="#">Privacy Policy</a><a href="#">Terms of Service</a><a href="#">Security</a><a href="#">Compliance</a></div>
  <div class="foot-rule"></div>
  <p class="copyright">2025 Tarnwell.com. VELMORAK™ - All rights reserved.</p>
</footer>

</body>
</html>
```